Need UI design for an iOS app game with most of the layout planned

The name of the game is "QUADRIX".

The goal of the game is to find a way to manipulate four numbers so that the end result is 24. Addition, subtraction, multiplication and division may be used and each number can only be used once.

The list of items we need is:

1. launch image, app icon, UI design of all scenes (10-12 scenes) of the app.
2. App background image should support screen size of both 640x1136.
3. Files are preferred to be in (.eps) format so that resolution can be adjusted later. But other file formats are welcome as long as resolution is high enough.
4. Icons, buttons, background image etc. should have their own file so that later they can be moved around in case design is changed.

The detailed requirement is in the attached file. The actual layout can vary if it can help achieve better result. We also attached several screenshots from iOS game "Glimtor". You can use that as your reference.

```html
<!DOCTYPE html>
<html lang="en">
<head>
<meta charset="utf-8">
<title>QUADRIX – Home Screen Variants</title>
<link rel="stylesheet" href="https://fonts.googleapis.com/css2?family=Aleo:wght@400;700&family=Lato:wght@300;400;700&display=swap">
<style>
  :root {
    --canvas-bg: #f2f2f2;
    --screen-bg: #ffffff;
    --ink: #222222;
    --icon-blue: #2aa7e0;
    --icon-grey: #c4c4c4;
    --footer-text: #b8b8b8;
    --divider: #d8d8d8;
    --title-ink: #c9f3ff;
    --hero-teal: #35a39c;
    --hero-cyan: #33a7c4;
    --hero-blue: #5a7fc4;
    --hero-purple: #7b3c8a;
    --btn-green: #48cb5f;
    --btn-red: #cb4f59;
    --btn-teal: #00a99c;
    --btn-violet: #8757a8;
    --btn-text: #ffffff;
  }

  * { box-sizing: border-box; margin: 0; padding: 0; }

  html, body {
    width: 1200px;
    height: 675px;
    overflow: hidden;
    background: var(--canvas-bg);
  }

  .board {
    position: relative;
    width: 1200px;
    height: 675px;
  }

  .screen {
    position: absolute;
    width: 281px;
    height: 502px;
    background: var(--screen-bg);
    display: flex;
    flex-direction: column;
  }
  .screen--classic { left: 77px; top: 67px; }
  .screen--alt { left: 590px; top: 63px; }

  .status-bar {
    height: 21px;
    display: flex;
    align-items: center;
    justify-content: space-between;
    padding: 0 8px;
    font-family: "Lato", sans-serif;
    font-size: 8px;
    font-weight: 700;
    color: var(--ink);
  }
  .status-bar__carrier { display: flex; gap: 4px; align-items: center; }
  .status-bar__signal { letter-spacing: -0.5px; font-size: 7px; }
  .status-bar__time { font-weight: 400; }
  .battery {
    width: 20px; height: 7px;
    border: 1px solid #9a9a9a;
    background: #eeeeee;
    position: relative;
  }
  .battery::after {
    content: "";
    position: absolute; right: -3px; top: 1.5px;
    width: 2px; height: 3px; background: #9a9a9a;
  }

  .nav-bar {
    height: 38px;
    display: flex;
    align-items: center;
    justify-content: space-between;
    padding: 0 6px 4px 7px;
  }
  .icon { display: block; }

  .hero {
    height: 230px;
    margin: 0 1px;
    display: flex;
    align-items: center;
    justify-content: center;
    background:
      radial-gradient(ellipse 65% 45% at 50% 100%, var(--hero-purple) 0%, rgba(123,60,138,0) 100%),
      radial-gradient(ellipse 70% 60% at 50% 55%, rgba(92,96,140,0.55) 0%, rgba(92,96,140,0) 100%),
      linear-gradient(135deg, var(--hero-teal) 0%, var(--hero-cyan) 45%, var(--hero-blue) 100%);
  }
  .hero__title {
    font-family: "Aleo", serif;
    font-weight: 700;
    font-size: 46px;
    letter-spacing: 1px;
    color: var(--title-ink);
  }

  .menu { display: flex; flex-direction: column; }
  .menu__button {
    height: 80px;
    display: flex;
    align-items: center;
    justify-content: center;
    font-family: "Aleo", serif;
    font-weight: 700;
    font-size: 19px;
    color: var(--btn-text);
  }
  .menu__button + .menu__button { height: 81px; }
  .screen--classic .menu__button--single { background: var(--btn-green); }
  .screen--classic .menu__button--multi { background: var(--btn-red); }
  .screen--alt .menu__button--single { background: var(--btn-teal); }
  .screen--alt .menu__button--multi { background: var(--btn-violet); }

  .footer {
    margin-top: 12px;
    flex: 1;
    border-top: 1px solid var(--divider);
    display: flex;
    align-items: center;
    justify-content: center;
    position: relative;
    font-family: "Lato", sans-serif;
    font-weight: 300;
    font-size: 12px;
    color: var(--footer-text);
  }
  .footer__settings {
    position: absolute;
    right: 10px;
    top: 50%;
    transform: translateY(-50%);
  }
</style>
</head>
<body>
<main class="board">

  <section class="screen screen--classic" aria-label="Home screen, settings in top bar">
    <div class="status-bar">
      <span class="status-bar__carrier">Net <span class="status-bar__signal">●●●●●</span></span>
      <span class="status-bar__time">11:20 AM</span>
      <span class="battery"></span>
    </div>
    <nav class="nav-bar">
      <svg class="icon icon--settings" width="24" height="24" viewBox="-12 -12 24 24" aria-label="Settings">
        <circle r="9" fill="none" stroke="var(--icon-blue)" stroke-width="5" stroke-dasharray="3.6 3.47"/>
        <circle r="7.5" fill="var(--icon-blue)"/>
        <circle r="3.4" fill="#ffffff"/>
      </svg>
      <svg class="icon icon--info" width="26" height="26" viewBox="0 0 26 26" aria-label="Information">
        <circle cx="13" cy="13" r="11.5" fill="none" stroke="var(--icon-blue)" stroke-width="1.6"/>
        <circle cx="13" cy="7.6" r="1.5" fill="var(--icon-blue)"/>
        <path d="M10.5 11h3.4v8h1.8M10.6 19h5.2" fill="none" stroke="var(--icon-blue)" stroke-width="1.6"/>
      </svg>
    </nav>
    <header class="hero">
      <h1 class="hero__title">QUADRIX</h1>
    </header>
    <div class="menu">
      <div class="menu__button menu__button--single">Single Player</div>
      <div class="menu__button menu__button--multi">Multi Player</div>
    </div>
    <footer class="footer">A game by Sample Name</footer>
  </section>

  <section class="screen screen--alt" aria-label="Home screen, settings in footer">
    <div class="status-bar">
      <span class="status-bar__carrier">Net <span class="status-bar__signal">●●●●●</span></span>
      <span class="status-bar__time">11:20 AM</span>
      <span class="battery"></span>
    </div>
    <nav class="nav-bar">
      <svg class="icon icon--back" width="20" height="24" viewBox="0 0 20 24" aria-label="Back">
        <path d="M13 4 L5 12 L13 20" fill="none" stroke="var(--icon-blue)" stroke-width="2.6" stroke-linecap="round" stroke-linejoin="round"/>
      </svg>
      <svg class="icon icon--info" width="26" height="26" viewBox="0 0 26 26" aria-label="Information">
        <circle cx="13" cy="13" r="11.5" fill="none" stroke="var(--icon-blue)" stroke-width="1.6"/>
        <circle cx="13" cy="7.6" r="1.5" fill="var(--icon-blue)"/>
        <path d="M10.5 11h3.4v8h1.8M10.6 19h5.2" fill="none" stroke="var(--icon-blue)" stroke-width="1.6"/>
      </svg>
    </nav>
    <header class="hero">
      <h1 class="hero__title">QUADRIX</h1>
    </header>
    <div class="menu">
      <div class="menu__button menu__button--single">Single Player</div>
      <div class="menu__button menu__button--multi">Multi Player</div>
    </div>
    <footer class="footer">
      A game by Sample Name
      <svg class="icon footer__settings" width="22" height="22" viewBox="-12 -12 24 24" aria-label="Settings">
        <circle r="9" fill="none" stroke="var(--icon-grey)" stroke-width="5" stroke-dasharray="3.6 3.47"/>
        <circle r="7.5" fill="var(--icon-grey)"/>
        <circle r="3.8" fill="#ffffff"/>
      </svg>
    </footer>
  </section>

</main>
</body>
</html>
```